Business Card Design

Very plain simple card, Plain modern font. Background. Grey fading to black. Large Bright lime green text. Saying.

TWR-ZA.COM

Small other details in white text.

Irish Horse Sales . Livery . Stud . Shows

Mark Dabrowski
TWR
Birch Lodge
Carrowmede Lane
Thistlecombe
Lincolnshire
LN4 7JX

Email. Twrzap@mailvale.co.uk
Tel. 07482 936504

Industry/Entity Type

Business

Contact Information for Business Card

As below

```html
<!DOCTYPE html>
<html lang="en">
<head>
<meta charset="utf-8">
<title>TWR-ZA.COM Business Card</title>
<link rel="stylesheet" href="https://fonts.googleapis.com/css2?family=Arimo:wght@400;700&family=Questrial&display=swap">
<style>
  :root {
    --page-bg: #ececec;
    --card-dark: #0e0e0e;
    --card-mid: #2b2b2b;
    --card-light: #5e5e5e;
    --lime: #e4f018;
    --ink-white: #f4f4f4;
    --ink-soft: #d8d8d8;
  }
  * { margin: 0; padding: 0; box-sizing: border-box; }
  html, body {
    width: 1200px;
    height: 900px;
    overflow: hidden;
    background: var(--page-bg);
  }
  .card {
    position: absolute;
    left: 100px;
    top: 164px;
    width: 1000px;
    height: 572px;
    background: linear-gradient(155deg, var(--card-dark) 0%, var(--card-mid) 45%, var(--card-light) 100%);
    color: var(--ink-white);
    font-family: "Arimo", Arial, sans-serif;
    box-shadow: 0 10px 30px rgba(0,0,0,0.25);
  }
  .brand {
    position: absolute;
    left: 96px;
    top: 128px;
    display: flex;
    align-items: center;
    gap: 22px;
  }
  .brand-square {
    width: 34px;
    height: 34px;
    background: var(--lime);
  }
  .brand-name {
    font-family: "Questrial", Arial, sans-serif;
    font-size: 94px;
    line-height: 1;
    color: var(--lime);
    letter-spacing: 1px;
  }
  .tagline {
    position: absolute;
    left: 156px;
    top: 240px;
    font-size: 28px;
    letter-spacing: 0.5px;
    color: var(--ink-white);
  }
  .contact-name {
    position: absolute;
    left: 156px;
    top: 290px;
    font-size: 25px;
    font-weight: 700;
  }
  .address {
    position: absolute;
    left: 156px;
    top: 332px;
    font-size: 18px;
    line-height: 23px;
    font-style: normal;
    color: var(--ink-soft);
  }
  .reach {
    position: absolute;
    left: 156px;
    top: 500px;
    font-size: 18px;
    line-height: 23px;
    color: var(--ink-soft);
  }
</style>
</head>
<body>
  <section class="card">
    <div class="brand">
      <span class="brand-square"></span>
      <span class="brand-name">TWR-ZA.COM</span>
    </div>
    <p class="tagline">Irish Horse Sales . Livery . Stud . Shows</p>
    <p class="contact-name">Mark Dabrowski</p>
    <address class="address">
      TWR<br>
      Birch Lodge<br>
      Carrowmede Lane<br>
      Thistlecombe<br>
      Lincolnshire<br>
      LN4 7JX
    </address>
    <p class="reach">
      Email. Twrzap@mailvale.co.uk<br>
      Tel. 07482 936504
    </p>
  </section>
</body>
</html>
```